Web page update/ Create new non flash site

I have a flash web page, created by my ex girlfriend through some kind of web design service. I want to take all of the information that I have on the page and put it together in a similar manner on a non-flash page.I want to add a lot of pictures, update the logo to the one i had made on pixel bazaar and reword a few things to reflect the the direction my business has gone in, in the past couple years since I made the site.. I also can't figure out why when people e-mail me from my page, I get the e-mail but no message, happens all the time and makes me think I'm losing business. My main problem is that I don't know what service was used in the past to create this page or what information someone would need to be able to work on it more. I also have another domain name that I want connected to it. the existing web page is at www.quillbyconstruction.net

Target Market(s)

I originally made this web page thinking that i was going to be in the remodeling business, but the majority of the work i get is for high end commercial and residential millwork and carpentry installations. I mainly will be advertising to other general contractors, but I want to keep the same feel that it has now, how it is mainly talking to homeowners that are thinking about hiring me to do some sort of project for them.

Industry/Entity Type

Business

Requirements
Must have
• Portfolio page needs to be updated to have LOTS more pictures and have them in an organized manner where it's easy to navigate through them. My other main thing is that I want to keep the same look and feel that it has with the nice woodgrain background, user friendly layout of links, etc.

```html
<!DOCTYPE html>
<html lang="en">
<head>
<meta charset="utf-8">
<title>Quillby Construction — building &amp; renovation company</title>
<link href="https://fonts.googleapis.com/css2?family=Baumans&family=Comfortaa:wght@400;700&family=Tinos&family=Arimo&display=swap" rel="stylesheet">
<style>
:root{
  --plank-a:#c27c3c;
  --plank-b:#b56d2f;
  --plank-c:#cb8746;
  --plank-seam:#8e4f1e;
  --header-wood:#d9a46d;
  --footer-wood:#d8a46d;
  --ink-light:#fff6e8;
  --ink-dark:#3b220f;
  --accent:#f4a43a;
  --caption:#e7e24b;
  --frame:#6e3516;
  --frame-light:#a35c2a;
}
*{box-sizing:border-box;margin:0;padding:0}
html,body{width:960px;height:1200px;overflow:hidden}
body{
  position:relative;
  font-family:"Arimo",Arial,sans-serif;
  background:
    repeating-linear-gradient(90deg,transparent 0 57px,var(--plank-seam) 57px 59px,transparent 59px 60px),
    repeating-linear-gradient(90deg,var(--plank-a) 0 60px,var(--plank-b) 60px 120px,var(--plank-c) 120px 180px,var(--plank-b) 180px 240px);
}
.abs{position:absolute}

/* header */
.site-header{position:absolute;left:0;top:0;width:960px;height:93px;
  background:
    repeating-linear-gradient(90deg,transparent 0 58px,rgba(140,80,30,.35) 58px 60px),
    var(--header-wood);
  box-shadow:0 4px 8px rgba(60,25,5,.45);}
.brand{position:absolute;left:89px;top:20px;font-family:"Baumans",sans-serif;font-size:31px;color:#f7dcae;letter-spacing:.5px}
.tagline{position:absolute;left:152px;top:55px;font-family:"Comfortaa",sans-serif;font-size:12px;color:#fff3e0}
.main-nav{position:absolute;left:0;top:0;font-family:"Comfortaa",sans-serif;font-size:11px;color:#3a2410}
.main-nav a{position:absolute;top:59px;color:inherit;text-decoration:none;white-space:nowrap}
.main-nav .current{left:467px;top:52px;width:81px;height:26px;border-radius:13px;background:#b9672a;color:#fff;
  text-align:center;line-height:26px;box-shadow:inset 0 1px 3px rgba(0,0,0,.3)}

/* slider */
.slide{position:absolute;border:4px solid #f3f3f3;box-shadow:0 8px 14px rgba(50,20,0,.45)}
.slide-side{border-color:#c9c9c9;border-width:3px}
.arrow{position:absolute;width:40px;height:40px}

/* services */
.section-title{position:absolute;left:0;top:496px;width:928px;text-align:center;font-family:"Comfortaa",sans-serif;font-size:22px;color:#fff}
.service-photo{position:absolute;width:194px;height:92px;border:2px solid #f2f2f2}
.service-photo span{position:absolute;left:0;right:0;bottom:6px;text-align:center;font-family:"Tinos",serif;font-size:15px;color:var(--caption)}
.service-text{position:absolute;width:197px;font-size:10px;line-height:14.4px;color:var(--ink-light);text-align:justify}
.shelf{position:absolute;left:80px;top:722px;width:800px;height:12px;border-radius:50%;background:rgba(80,35,5,.55);filter:blur(2px)}
.more{position:absolute;top:724px;width:70px;height:32px;background:var(--accent);color:#fff;font-size:8.5px;font-weight:bold;
  text-align:center;line-height:26px;clip-path:polygon(0 0,100% 0,100% 100%,50% 84%,0 100%)}

/* gallery */
.gallery-panel{position:absolute;left:83px;top:804px;width:783px;height:188px;border-radius:10px;background:rgba(238,196,150,.55);box-shadow:0 3px 6px rgba(60,25,5,.3)}
.gallery-frame{position:absolute;top:822px;width:167px;height:141px;background:linear-gradient(135deg,var(--frame-light),var(--frame));
  border:2px solid #4b220b;box-shadow:0 8px 8px -4px rgba(50,20,0,.5)}
.gallery-frame div{position:absolute;left:13px;top:13px;right:13px;bottom:13px;border:2px solid #2c1307}

/* footer */
.site-footer{position:absolute;left:0;top:1028px;width:960px;height:172px;
  background:repeating-linear-gradient(90deg,transparent 0 58px,rgba(140,80,30,.25) 58px 60px),var(--footer-wood)}
.footer-edge{position:absolute;left:0;top:1022px}
.footer-col{position:absolute;top:1044px;color:var(--ink-dark);font-family:"Comfortaa",sans-serif}
.footer-col h3{font-family:"Baumans",sans-serif;font-weight:normal;font-size:17px;margin-bottom:6px}
.footer-col li{list-style:none;font-size:9.5px;height:19.2px;padding-left:14px;position:relative}
.footer-col li::before{content:"";position:absolute;left:2px;top:4px;width:5px;height:5px;border-radius:50%;background:var(--ink-dark)}
.news p{font-size:9.5px;line-height:17.6px}
.legal{position:absolute;top:1176px;font-family:"Comfortaa",sans-serif;font-size:9.5px;color:var(--ink-dark)}
</style>
</head>
<body>

<header class="site-header">
  <div class="brand">Quillby Construction</div>
  <div class="tagline">building &amp; renovation company</div>
  <nav class="main-nav">
    <a class="current" href="#">About us</a>
    <a href="#" style="left:572px">Services</a>
    <a href="#" style="left:657px">Portfolio</a>
    <a href="#" style="left:743px">Process</a>
    <a href="#" style="left:825px">Contact</a>
  </nav>
</header>

<!-- showcase slider -->
<div class="slide slide-side" style="left:130px;top:184px;width:96px;height:208px;background:linear-gradient(160deg,#e6e2dc,#b96f33 55%,#9a7a58)" role="img" aria-label="Bedroom with orange bedding"></div>
<div class="slide slide-side" style="left:738px;top:184px;width:98px;height:208px;background:linear-gradient(200deg,#6a6462,#d9d6d2 50%,#262220)" role="img" aria-label="Modern bathroom with dark vanity"></div>
<div class="slide" style="left:221px;top:117px;width:522px;height:338px;background:linear-gradient(180deg,#8a3b1c 0%,#a5512c 45%,#c98466 75%,#4a1810 100%)" role="img" aria-label="Living room with leather sofa and armchairs"></div>
<svg class="arrow" style="left:108px;top:268px" viewBox="0 0 40 40"><circle cx="20" cy="20" r="18" fill="#f1f1f1" stroke="#8d8d8d" stroke-width="2"/><circle cx="20" cy="20" r="13" fill="#fff" stroke="#bbb"/><path d="M23 13 L14 20 L23 27Z" fill="#333"/></svg>
<svg class="arrow" style="left:814px;top:268px" viewBox="0 0 40 40"><circle cx="20" cy="20" r="18" fill="#f1f1f1" stroke="#8d8d8d" stroke-width="2"/><circle cx="20" cy="20" r="13" fill="#fff" stroke="#bbb"/><path d="M17 13 L26 20 L17 27Z" fill="#333"/></svg>

<!-- services -->
<svg class="abs" style="left:94px;top:502px" width="760" height="16" viewBox="0 0 760 16">
  <line x1="20" y1="8" x2="302" y2="8" stroke="#f0c896" stroke-width="1"/>
  <line x1="446" y1="8" x2="740" y2="8" stroke="#f0c896" stroke-width="1"/>
  <path d="M2 8 L12 3 L9 8 L12 13Z M10 8 H18" fill="#fff" stroke="#fff"/>
  <path d="M758 8 L748 3 L751 8 L748 13Z M750 8 H742" fill="#fff" stroke="#fff"/>
</svg>
<h2 class="section-title" style="font-weight:normal">Our Services</h2>

<div class="service-photo" style="left:101px;top:534px;background:linear-gradient(180deg,#e8e6e2,#bdb8b0 60%,#3a3432)" role="img" aria-label="Bedroom furniture"><span>Bedroom furniture</span></div>
<div class="service-photo" style="left:366px;top:534px;background:linear-gradient(180deg,#dfe6e4,#c9bfae 55%,#3a332c)" role="img" aria-label="Living room furniture"><span>Living room furniture</span></div>
<div class="service-photo" style="left:639px;top:534px;background:linear-gradient(180deg,#cfc6b8,#4c4a48 55%,#1e1c1a)" role="img" aria-label="Office furniture"><span>Office Furniture</span></div>

<p class="service-text" style="left:102px;top:636px">If you can dream it, we can build it. Quillby Construction has its roots in home renovations, remodeling, additions and all forms of custom carpentry fabrications and installations.</p>
<p class="service-text" style="left:370px;top:644px">Our building team has serviced high end clientele in all of the most prestigious areas of our great city and we are certain that we can make a happy customer out of you,</p>
<p class="service-text" style="left:644px;top:644px">Although our core work is in remodeling and millwork installations, we offer a wide range of services in all trades of construction.</p>

<div class="shelf"></div>
<a class="more" href="#" style="left:168px">more details</a>
<a class="more" href="#" style="left:436px">more details</a>
<a class="more" href="#" style="left:712px">more details</a>

<!-- gallery -->
<div class="gallery-panel"></div>
<div class="gallery-frame" style="left:110px"><div style="background:linear-gradient(180deg,#7d8a96,#9aa0a8 60%,#6c6f8a)" role="img" aria-label="Room with yellow lounge chair"></div></div>
<div class="gallery-frame" style="left:296px"><div style="background:linear-gradient(180deg,#e9d6a6,#d9a35c 55%,#b0572a)" role="img" aria-label="Children's bedroom with bunk bed"></div></div>
<div class="gallery-frame" style="left:484px"><div style="background:linear-gradient(180deg,#e6eef2,#c0a27a 55%,#8c6a48)" role="img" aria-label="Lounge with sofas by the windows"></div></div>
<div class="gallery-frame" style="left:673px"><div style="background:linear-gradient(180deg,#eef0ec,#9dc4a8 40%,#8a5a3a 80%)" role="img" aria-label="Modern kitchen with island"></div></div>

<!-- footer -->
<svg class="footer-edge" width="960" height="8" viewBox="0 0 960 8" preserveAspectRatio="none">
  <path fill="#d8a46d" d="M0 8 L0 4 L4 0 L8 4 L12 0 L16 4 L20 0 L24 4 L28 0 L32 4 L36 0 L40 4 L44 0 L48 4 L52 0 L56 4 L60 0 L64 4 L68 0 L72 4 L76 0 L80 4 L84 0 L88 4 L92 0 L96 4 L100 0 L104 4 L108 0 L112 4 L116 0 L120 4 L124 0 L128 4 L132 0 L136 4 L140 0 L144 4 L148 0 L152 4 L156 0 L160 4 L164 0 L168 4 L172 0 L176 4 L180 0 L184 4 L188 0 L192 4 L196 0 L200 4 L204 0 L208 4 L212 0 L216 4 L220 0 L224 4 L228 0 L232 4 L236 0 L240 4 L244 0 L248 4 L252 0 L256 4 L260 0 L264 4 L268 0 L272 4 L276 0 L280 4 L284 0 L288 4 L292 0 L296 4 L300 0 L304 4 L308 0 L312 4 L316 0 L320 4 L324 0 L328 4 L332 0 L336 4 L340 0 L344 4 L348 0 L352 4 L356 0 L360 4 L364 0 L368 4 L372 0 L376 4 L380 0 L384 4 L388 0 L392 4 L396 0 L400 4 L404 0 L408 4 L412 0 L416 4 L420 0 L424 4 L428 0 L432 4 L436 0 L440 4 L444 0 L448 4 L452 0 L456 4 L460 0 L464 4 L468 0 L472 4 L476 0 L480 4 L484 0 L488 4 L492 0 L496 4 L500 0 L504 4 L508 0 L512 4 L516 0 L520 4 L524 0 L528 4 L532 0 L536 4 L540 0 L544 4 L548 0 L552 4 L556 0 L560 4 L564 0 L568 4 L572 0 L576 4 L580 0 L584 4 L588 0 L592 4 L596 0 L600 4 L604 0 L608 4 L612 0 L616 4 L620 0 L624 4 L628 0 L632 4 L636 0 L640 4 L644 0 L648 4 L652 0 L656 4 L660 0 L664 4 L668 0 L672 4 L676 0 L680 4 L684 0 L688 4 L692 0 L696 4 L700 0 L704 4 L708 0 L712 4 L716 0 L720 4 L724 0 L728 4 L732 0 L736 4 L740 0 L744 4 L748 0 L752 4 L756 0 L760 4 L764 0 L768 4 L772 0 L776 4 L780 0 L784 4 L788 0 L792 4 L796 0 L800 4 L804 0 L808 4 L812 0 L816 4 L820 0 L824 4 L828 0 L832 4 L836 0 L840 4 L844 0 L848 4 L852 0 L856 4 L860 0 L864 4 L868 0 L872 4 L876 0 L880 4 L884 0 L888 4 L892 0 L896 4 L900 0 L904 4 L908 0 L912 4 L916 0 L920 4 L924 0 L928 4 L932 0 L936 4 L940 0 L944 4 L948 0 L952 4 L956 0 L960 4 L960 8Z"/>
</svg>
<footer class="site-footer"></footer>

<div class="footer-col" style="left:89px">
  <h3>About us</h3>
  <ul><li>Stonevale Australia</li><li>Environmental Commitment</li><li>Careers &amp; Opportunities</li><li>Office Locations</li></ul>
</div>
<div class="footer-col" style="left:261px">
  <h3>Applications</h3>
  <ul><li>Kitchen</li><li>Bathroom</li><li>Commercial</li><li>Furniture</li></ul>
</div>
<div class="footer-col" style="left:404px">
  <h3>Products</h3>
  <ul><li>Stonevale Classico</li><li>Stonevale Motivo</li><li>Stonevale Supremo</li><li>Stonevale Concetto</li></ul>
</div>
<div class="footer-col" style="left:568px">
  <h3>Gallery</h3>
  <ul><li>Residential Gallery</li><li>Commercial Gallery</li><li>Projects</li></ul>
</div>
<div class="footer-col news" style="left:712px">
  <h3>Latest news</h3>
  <p>&nbsp;07.02.11 &nbsp;&nbsp;GLASSVIEW</p>
  <p>&nbsp;</p>
  <p>&nbsp;Our newest product Glassview high<br>&nbsp;&nbsp;resolution images printed<br>&nbsp;&nbsp;onto glass is...</p>
</div>

<div class="legal" style="left:88px">Copyright © Quillby Construction 2010 - 2011. All Rights Reserved.</div>
<div class="legal" style="left:620px;top:1181px">Terms &amp; Conditions &nbsp;&nbsp;| &nbsp;&nbsp;Terms of Use &nbsp;&nbsp;| &nbsp;&nbsp;Privacy policy</div>

</body>
</html>
```